Beacon Law Stationary - Law Firm

I am looking for a designer who can help me design letterhead and envelopes consistent with our new business cards. Feel free to reach out to me directly at ned@beaconlawgroup.example. Thank you!! Visit beaconlawgroup.example to see our site and the attached files for creative assets.

Target Market(s)

Anyone needing a lawyer

Font styles to use
Other font styles liked:
• Adobe Caslon Pro

Requirements
Must have
• Adobe Caslon Pro font
Full color
Nice to have
• My photo on front along with 2/3 face of camo - see mock up for example of what I have in mind.

American colors - similar to the ones found on my website and gold.

```html
<!DOCTYPE html>
<html lang="en">
<head>
<meta charset="utf-8">
<title>Beacon Law Stationery</title>
<link href="https://fonts.googleapis.com/css2?family=Libre+Caslon+Text&family=Poppins:wght@300;400&display=swap" rel="stylesheet">
<style>
  :root {
    --backdrop: #6e6e6e;
    --paper: #f4f4f2;
    --navy: #0c2246;
    --gold: #a99a55;
    --ink: #3c3c3c;
    --faint: #e6e6e4;
  }
  * { margin: 0; padding: 0; box-sizing: border-box; }
  html, body { width: 1200px; height: 755px; overflow: hidden; background: var(--backdrop); }
  .stage { position: relative; width: 1200px; height: 755px; }
  .sheet { position: absolute; background: var(--paper); overflow: hidden; box-shadow: 0 1px 4px rgba(0,0,0,.25); }
  .wordmark {
    position: absolute; font-family: "Libre Caslon Text", serif; color: var(--gold);
    font-size: 14.5px; line-height: 15px; letter-spacing: 1.4px;
  }
  .header-band { position: absolute; left: 0; top: 0; }
  .crest-watermark { position: absolute; background: linear-gradient(180deg, #efefed, var(--faint)); border-radius: 40px 40px 110px 110px; opacity: .8; }

  .letterhead { left: 92px; top: 62px; width: 447px; height: 630px; }
  .letterhead .wordmark { left: 78px; top: 36px; }
  .letter { position: absolute; left: 47px; top: 150px; width: 351px; font-family: "Poppins", sans-serif; color: var(--ink); }
  .salutation { font-size: 12.5px; font-weight: 300; margin-bottom: 12px; }
  .letter p { font-size: 7.6px; font-weight: 300; line-height: 13px; text-align: justify; hyphens: auto; margin-bottom: 13px; }
  .letter .closing { margin-top: -2px; margin-bottom: 0; }

  .contact { position: absolute; font-family: "Poppins", sans-serif; font-size: 7.6px; line-height: 9.2px; color: var(--ink); font-weight: 300; }
  .contact .firm { color: var(--navy); font-weight: 400; }
  .contact-lines div { display: flex; align-items: center; gap: 4px; }
  .contact-lines svg { width: 6px; height: 6px; fill: var(--navy); flex: none; }

  .envelope-back { width: 498px; height: 246px; }
  .envelope-back .flap { position: absolute; left: 0; top: 0; }
  .flap-name { position: absolute; left: 0; width: 100%; text-align: center; font-family: "Libre Caslon Text", serif; font-size: 9px; letter-spacing: 1.2px; }
  .envelope-gold { left: 573px; top: 168px; }
  .envelope-gold .flap-name { top: 32px; color: var(--navy); }
  .envelope-navy { left: 624px; top: 307px; }
  .envelope-navy .flap-name { top: 33px; color: var(--gold); }

  .envelope-front { left: 573px; top: 446px; width: 498px; height: 246px; }
  .envelope-front .wordmark { left: 60px; top: 30px; }
</style>
</head>
<body>
<div class="stage">

  <section class="sheet letterhead">
    <svg class="header-band" width="447" height="95" viewBox="0 0 447 95">
      <path d="M0 0H208C200 50 170 92 110 92H0Z" fill="var(--gold)"/>
      <path d="M0 0H202C194 48 160 90 100 91H0Z" fill="var(--navy)"/>
    </svg>
    <div class="wordmark">BEACON<br>LAW</div>
    <div class="crest-watermark" role="img" aria-label="Faint crest watermark" style="left:226px;top:220px;width:221px;height:402px;"></div>
    <div class="letter">
      <div class="salutation">Dear Mr. Carter,</div>
      <p>Lorem ipsum dolor sit amet, consectetur adipiscing elit. Donec orci purus, luctus vitae dignissim eu, iaculis sed purus. Vivamus faucibus, ipsum nec aliquet viverra, leo mauris condimentum ligula, sit amet sagittis enim ligula quis arcu. Nam egestas tortor id nisi porttitor mattis. In tortor ante, ultricies in suscipit a, tempus non massa. Vivamus et auctor mi. Fusce vel massa nulla. Phasellus nec eros mauris, et scelerisque orci.</p>
      <p>Donec malesuada orci vitae nulla accumsan porta a id massa. Quisque accumsan iaculis magna sit amet fringilla. Maecenas consequat, magna eget tincidunt semper, odio nibh rutrum mi, id feugiat ante nisi eu risus. Vestibulum nunc orci, rhoncus a placerat in, ultricies in mi. Cras mattis varius eros, vel fringilla nisi suscipit eget. Quisque scelerisque sagittis nulla at porttitor.</p>
      <p>Sed id augue vitae urna euismod commodo aliquet a quam. Pellentesque arcu velit, cursus et malesuada ut, consequat et diam. Nullam erat sem, rhoncus id ullamcorper vitae, rhoncus et arcu. In ultricies ultricies nulla, ut rutrum nisi iaculis at. Donec eu magna a metus ornare faucibus. Fusce aliquet faucibus ultricies. Morbi semper, est id tincidunt gravida, sem arcu adipiscing lacus, ac bibendum nulla leo eu purus. Quisque nec diam sed risus consectetur a ccumsan quis quis nibh. Vestibulum id purus lorem.</p>
      <p>It is a long established fact that a reader will be distracted by the readable content of a page when looking at its layout. The point of using Lorem Ipsum is that it has a more-or-less normal distribution of letters, as opposed to using 'Content here, content here', making it look like readable English. Many desktop publishing packages</p>
      <p class="closing">Sincerely,</p>
    </div>
    <div class="contact" style="left:47px;top:571px;">
      <div class="firm">Beacon Law Inc</div>
      <div>48 Harbor Lane</div>
      <div>Easton, Ohio 45000</div>
    </div>
    <div class="contact contact-lines" style="left:163px;top:571px;">
      <div><svg viewBox="0 0 10 10"><path d="M2 0l2 2-1 2c1 1.5 2 2.5 3 3l2-1 2 2-2 2C4 9 1 6 0 2z"/></svg>(555)010-2291</div>
      <div><svg viewBox="0 0 10 10"><path d="M0 2h10v6H0zM0 2l5 3 5-3"/></svg>mara@beaconlawgroup.example</div>
      <div><svg viewBox="0 0 10 10"><circle cx="5" cy="5" r="4.5" fill="none" stroke="var(--navy)"/><path d="M0.5 5h9M5 .5v9" stroke="var(--navy)"/></svg>www.beaconlawgroup.example</div>
    </div>
  </section>

  <section class="sheet envelope-back envelope-gold">
    <svg class="flap" width="498" height="80" viewBox="0 0 498 80">
      <path d="M0 0H498L490 42Q485 79 455 79H43Q13 79 8 42Z" fill="var(--gold)"/>
    </svg>
    <div class="flap-name">BEACON LAW</div>
  </section>

  <section class="sheet envelope-back envelope-navy">
    <svg class="flap" width="498" height="80" viewBox="0 0 498 80">
      <path d="M0 0H498L490 42Q485 79 455 79H43Q13 79 8 42Z" fill="var(--navy)"/>
    </svg>
    <div class="flap-name">BEACON LAW</div>
  </section>

  <section class="sheet envelope-front">
    <svg class="header-band" width="498" height="95" viewBox="0 0 498 95">
      <path d="M0 0H190C183 50 155 92 100 92H0Z" fill="var(--gold)"/>
      <path d="M0 0H185C178 48 148 90 92 91H0Z" fill="var(--navy)"/>
    </svg>
    <div class="wordmark">BEACON<br>LAW</div>
    <div class="crest-watermark" role="img" aria-label="Faint crest watermark" style="left:369px;top:10px;width:129px;height:236px;"></div>
    <div class="contact" style="left:36px;top:187px;">
      <div class="firm">Beacon Law Inc</div>
      <div>48 Harbor Lane</div>
      <div>Easton, Ohio 45000</div>
    </div>
    <div class="contact contact-lines" style="left:150px;top:187px;">
      <div><svg viewBox="0 0 10 10"><path d="M2 0l2 2-1 2c1 1.5 2 2.5 3 3l2-1 2 2-2 2C4 9 1 6 0 2z"/></svg>(555)010-2291</div>
      <div><svg viewBox="0 0 10 10"><path d="M0 2h10v6H0zM0 2l5 3 5-3"/></svg>mara@beaconlawgroup.example</div>
      <div><svg viewBox="0 0 10 10"><circle cx="5" cy="5" r="4.5" fill="none" stroke="var(--navy)"/><path d="M0.5 5h9M5 .5v9" stroke="var(--navy)"/></svg>www.beaconlawgroup.example</div>
    </div>
  </section>

</div>
</body>
</html>
```